Halvorn spray foam and Environmental

I have business cards but need new ones. The ones I have are very bland. Here is. Y company website http://www.halvornsprayfoam.ca

Also I can send you copies of the current cards
I would also need my current logo on the new design as well.. Also spray foam and Environmental

Industry/Entity Type

Business

Logo Text

Halvorn.

```html
<!DOCTYPE html>
<html lang="en">
<head>
<meta charset="utf-8">
<title>Halvorn Spray Foam &amp; Environmental – Business Card</title>
<link rel="stylesheet" href="https://fonts.googleapis.com/css2?family=Roboto:ital,wght@0,400;0,700;0,900;1,900&family=Tinos&display=swap">
<style>
  :root{
    --purple:#744a8c;
    --purple-dark:#5e3773;
    --green:#4db443;
    --grey:#8d8d8d;
    --grey-dark:#555;
    --text:#333;
    --white:#fff;
    --bg:#e9e9ec;
  }
  *{box-sizing:border-box;margin:0;padding:0}
  html,body{width:1200px;height:880px;overflow:hidden;background:var(--bg);font-family:"Roboto",Arial,sans-serif}
  .card{position:absolute;left:290px;width:620px;height:354px;border-radius:18px;overflow:hidden;box-shadow:0 8px 24px rgba(0,0,0,.18)}
  .card--front{top:46px;background:var(--white)}
  .card--back{top:474px;background:var(--purple)}

  /* front */
  .front-bands{position:absolute;left:0;top:0}
  .divider{position:absolute;left:318px;top:36px;width:1px;height:170px;background:#ccc}
  .brand{position:absolute;display:flex;align-items:flex-start;gap:8px}
  .brand__mark{width:24px;height:24px;background:var(--purple);margin-top:2px}
  .brand__name{font-weight:900;font-size:22px;color:var(--purple);letter-spacing:.5px;line-height:1}
  .brand__sub{font-weight:700;font-size:8px;color:var(--purple);letter-spacing:.6px;margin-top:2px}
  .brand__sub--env{color:var(--green)}
  .brand__tag{font-family:"Tinos",serif;font-size:12px;color:var(--grey);margin-top:1px}
  .brand__tag--env{color:var(--green)}
  .brand--foam{left:70px;top:56px}
  .brand--env{left:380px;top:40px}
  .rule{position:absolute;height:1px;background:#bbb}
  .rule--foam{left:20px;top:120px;width:230px}
  .rule--env{left:340px;top:104px;width:260px}
  .contacts{position:absolute;list-style:none;font-size:14px;color:var(--text);line-height:21px}
  .contacts li{display:flex;align-items:center;gap:8px;justify-content:flex-end}
  .contacts--foam{right:318px;top:138px}
  .contacts--env{left:352px;top:122px}
  .contacts--env li{justify-content:flex-start;flex-direction:row-reverse}
  .icon{width:17px;height:17px;background:var(--purple);display:flex;align-items:center;justify-content:center;flex:none}
  .address{position:absolute;left:0;right:0;top:238px;text-align:center;font-size:15px;color:var(--text)}

  /* back */
  .back-edge{position:absolute;left:0;top:0;width:22px;height:100%;background:var(--white)}
  .back-edge-line{position:absolute;left:30px;top:0;width:3px;height:100%;background:var(--white)}
  .social{position:absolute;right:40px;top:26px;display:flex;gap:10px}
  .social span{width:26px;height:26px;border-radius:3px;background:var(--white)}
  .section{position:absolute;left:60px;right:40px;color:var(--white)}
  .section--foam{top:82px}
  .section--env{top:200px}
  .section__title{font-weight:900;font-style:italic;font-size:25px;letter-spacing:.3px}
  .section__head{display:flex;align-items:center;gap:10px;margin-top:10px}
  .section__label{font-weight:700;font-size:14px;white-space:nowrap}
  .section__line{flex:1;height:1px;background:rgba(255,255,255,.8)}
  .services{list-style:none;display:flex;flex-wrap:wrap;gap:3px 14px;font-size:14px;margin-top:6px}
  .services li::before{content:"•";margin-right:4px}
  .split{position:absolute;left:33px;right:0;top:182px;height:2px;background:rgba(255,255,255,.85)}
</style>
</head>
<body>

<section class="card card--front" aria-label="Card front">
  <svg class="front-bands" width="620" height="354" viewBox="0 0 620 354" aria-hidden="true">
    <rect x="0" y="334" width="620" height="20" fill="#744a8c"/>
    <rect x="0" y="326" width="310" height="3" fill="#555"/>
    <rect x="310" y="304" width="310" height="50" fill="#744a8c"/>
    <rect x="310" y="300" width="310" height="3" fill="#4db443"/>
  </svg>

  <div class="brand brand--foam">
    <span class="brand__mark"></span>
    <div>
      <div class="brand__name">HALVORN</div>
      <div class="brand__sub">SPRAY FOAM LTD.</div>
      <div class="brand__tag">Residential &amp; Commercial</div>
    </div>
  </div>
  <div class="rule rule--foam"></div>

  <div class="divider"></div>

  <div class="brand brand--env">
    <span class="brand__mark"></span>
    <div>
      <div class="brand__name">HALVORN</div>
      <div class="brand__sub brand__sub--env">ENVIRONMENTAL</div>
      <div class="brand__tag brand__tag--env">Residential &amp; Commercial</div>
    </div>
  </div>
  <div class="rule rule--env"></div>

  <ul class="contacts contacts--foam">
    <li>604-555-0142 <span class="icon"><svg width="11" height="11" viewBox="0 0 12 12"><path d="M2 1h3l1 3-2 1c1 2 2 3 3 3l1-2 3 1v3c-6 1-10-4-9-9z" fill="#fff"/></svg></span></li>
    <li>halvornfoam@mailbox.ca <span class="icon"><svg width="11" height="9" viewBox="0 0 12 9"><rect x=".5" y=".5" width="11" height="8" fill="none" stroke="#fff"/><path d="M.5.5 6 5l5.5-4.5" fill="none" stroke="#fff"/></svg></span></li>
    <li>www.halvornsprayfoam.ca <span class="icon"><svg width="11" height="11" viewBox="0 0 12 12"><circle cx="6" cy="6" r="5" fill="none" stroke="#fff"/><path d="M1 6h10M6 1c-3 3-3 7 0 10M6 1c3 3 3 7 0 10" fill="none" stroke="#fff"/></svg></span></li>
  </ul>

  <ul class="contacts contacts--env">
    <li>604-555-0187 <span class="icon"><svg width="11" height="11" viewBox="0 0 12 12"><path d="M2 1h3l1 3-2 1c1 2 2 3 3 3l1-2 3 1v3c-6 1-10-4-9-9z" fill="#fff"/></svg></span></li>
    <li>halvornenviro1@mailbox.ca <span class="icon"><svg width="11" height="9" viewBox="0 0 12 9"><rect x=".5" y=".5" width="11" height="8" fill="none" stroke="#fff"/><path d="M.5.5 6 5l5.5-4.5" fill="none" stroke="#fff"/></svg></span></li>
    <li>www.halvornenvironmental.ca <span class="icon"><svg width="11" height="11" viewBox="0 0 12 12"><circle cx="6" cy="6" r="5" fill="none" stroke="#fff"/><path d="M1 6h10M6 1c-3 3-3 7 0 10M6 1c3 3 3 7 0 10" fill="none" stroke="#fff"/></svg></span></li>
  </ul>

  <p class="address">4820 Larchmont Ave Burnaby, British Columbia V5H 2K9, CA</p>
</section>

<section class="card card--back" aria-label="Card back">
  <div class="back-edge"></div>
  <div class="back-edge-line"></div>
  <div class="social" aria-label="Social profiles"><span></span><span></span></div>

  <div class="section section--foam">
    <h2 class="section__title">Halvorn Spray Foam</h2>
    <div class="section__head"><span class="section__label">Our Services</span><span class="section__line"></span></div>
    <ul class="services">
      <li>Residential Spray Foam</li>
      <li>Commercial Spray Foam</li>
      <li>Why Spray Foam?</li>
      <li>Types Of Insulation</li>
    </ul>
  </div>

  <div class="split"></div>

  <div class="section section--env">
    <h2 class="section__title">Halvorn Environmental</h2>
    <div class="section__head"><span class="section__label">Our Services</span><span class="section__line"></span></div>
    <ul class="services">
      <li>Asbestos Testing</li>
      <li>Abestos Removal</li>
      <li>Mould Removal</li>
      <li>Insulation Removal</li>
      <li>Grow-OP Cleanup</li>
      <li>Lead Abatement</li>
    </ul>
  </div>
</section>

</body>
</html>
```